Design a flyer to be given to attendees of a STEM teacher conference.

Design a flyer for Verdan Fabrication's 3D-printing consumables.

Target Market(s)

Education, Technology

Industry/Entity Type

Technology

Colors
00AB8E
00BBA5
67D7C9
C6EFE9
E9F9F6

Requirements
Must have
• The key points in the pdf file. Our logo.
Nice to have
• Some product picture from our website www.verdanfab.com.au

```html
<!DOCTYPE html>
<html lang="en">
<head>
<meta charset="utf-8">
<title>Verdan Fabrication – STEM Conference Flyer</title>
<link rel="stylesheet" href="https://fonts.googleapis.com/css2?family=Rubik:ital,wght@0,400;0,500;0,700;1,400&display=swap">
<style>
  :root {
    --teal-deep: #00AB8E;
    --teal: #00BBA5;
    --teal-soft: #67D7C9;
    --teal-pale: #C6EFE9;
    --teal-mist: #E9F9F6;
    --ink: #0d0d0d;
    --white: #ffffff;
    --backdrop: #f2f2f2;
  }
  * { box-sizing: border-box; margin: 0; padding: 0; }
  html, body {
    width: 1200px; height: 1200px; overflow: hidden;
    background: var(--backdrop);
    font-family: "Rubik", Arial, sans-serif;
  }
  .flyer {
    position: absolute; left: 202px; top: 38px;
    width: 796px; height: 1123px;
    background: var(--white);
    overflow: hidden;
  }
  .brand {
    position: absolute; top: 92px; left: 0; width: 100%;
    display: flex; justify-content: center; align-items: center; gap: 22px;
  }
  .brand-mark { width: 64px; height: 64px; background: var(--teal-deep); border-radius: 6px; }
  .brand-name {
    font-weight: 500; font-size: 44px; letter-spacing: 4px;
    color: var(--ink); text-transform: uppercase;
  }
  .headline {
    position: absolute; top: 252px; left: 0; width: 100%;
    text-align: center; color: var(--ink); text-transform: uppercase;
    font-weight: 400; font-size: 52px; line-height: 58px; letter-spacing: -0.5px;
  }
  .headline .accent { color: var(--teal-deep); font-weight: 700; font-size: 58px; }
  .headline .strong { font-weight: 500; }
  .panel {
    position: absolute; left: 0; top: 471px; width: 100%; height: 652px;
    background: radial-gradient(ellipse 70% 55% at 0% 100%, var(--teal-soft) 0%, rgba(103,215,201,0) 70%), var(--teal-deep);
  }
  .tag {
    position: absolute; left: 50%; transform: translateX(-50%);
    background: var(--ink); color: var(--white);
    border-radius: 12px; font-weight: 500; font-size: 22px;
    display: flex; align-items: center; justify-content: center; white-space: nowrap;
  }
  .tag-education { top: 3px; width: 566px; height: 62px; }
  .tag-why { top: 210px; width: 470px; height: 61px; }
  .points-italic {
    position: absolute; top: 80px; left: 0; width: 100%;
    color: var(--white); font-style: italic; font-size: 14.5px; line-height: 19px; text-align: center;
  }
  .points-italic .line { display: block; white-space: nowrap; }
  .points-italic p + p { margin-top: 19px; }
  .points-list {
    position: absolute; top: 282px; left: 0; width: 100%;
    list-style: none; text-align: center; color: var(--white); font-size: 16px; line-height: 27px;
    white-space: nowrap;
  }
  .offer {
    position: absolute; left: 47px; top: 384px; width: 699px; height: 130px;
    background: rgba(198,239,233,0.55); border-radius: 18px;
    box-shadow: 6px 8px 14px rgba(0,0,0,0.28);
    text-align: center; color: var(--white);
  }
  .offer-title { margin-top: 22px; font-size: 22px; font-weight: 500; }
  .offer-deal { margin-top: 14px; font-size: 22px; white-space: nowrap; }
  .offer-deal .amount { color: var(--ink); font-weight: 700; font-size: 31px; }
  .offer-deal .code { font-weight: 700; font-style: italic; }
  .contact { position: absolute; top: 552px; left: 0; width: 100%; text-align: center; color: var(--white); }
  .contact-title { font-weight: 700; font-size: 22px; }
  .contact-line { margin-top: 10px; font-size: 16px; white-space: nowrap; }
  .contact-line .sep { margin: 0 10px; }
</style>
</head>
<body>
  <main class="flyer">
    <header class="brand">
      <span class="brand-mark"></span>
      <span class="brand-name">Verdan Fabrication</span>
    </header>

    <h1 class="headline">
      Unlock the future of<br>
      <span class="accent">3D Printing</span> with<br>
      <span class="strong">Verdan Fabrication</span>
    </h1>

    <section class="panel">
      <h2 class="tag tag-education">High-Quality Filaments for STEM Education</h2>
      <div class="points-italic">
        <p><span class="line">Durable and Reliable: Our filaments ensure consistent, high-quality prints every time—</span><span class="line">ideal for classroom projects.</span></p>
        <p><span class="line">Eco-Friendly Options: Choose from our range of sustainable materials, helping schools</span><span class="line">meet green initiatives.</span></p>
      </div>

      <h2 class="tag tag-why">Why Verdan Fabrication Filaments?</h2>
      <ul class="points-list">
        <li>Aesthetic Filaments: Perfect for eye-catching, professional-looking classroom models.</li>
        <li>Reliable &amp; Durable: Consistent prints for hands-on STEM projects.</li>
        <li>Eco-Friendly Options: Choose sustainable materials for a greener classroom.</li>
      </ul>

      <div class="offer">
        <p class="offer-title">Exclusive Offer for Forum Attendees</p>
        <p class="offer-deal"><span class="amount">10% OFF</span> with code <span class="code">QUANTUM</span> on your first order!</p>
      </div>

      <footer class="contact">
        <p class="contact-title">CONTACT US:</p>
        <p class="contact-line">03 9000 4821<span class="sep">|</span>sales@verdanfab.com.au<span class="sep">|</span>www.verdanfab.com.au</p>
      </footer>
    </section>
  </main>
</body>
</html>
```